Display Layouts per segment use-cases

21.5in portrait (9:16) x 2
Office towers
Hotels
Shopping Malls

Target Market(s)

Office towers / Hotels / Shopping Malls

```html
<!DOCTYPE html>
<html lang="en">
<head>
<meta charset="utf-8">
<title>Display Layouts per Segment</title>
<link rel="stylesheet" href="https://fonts.googleapis.com/css2?family=Barlow:wght@400;500;600&family=Barlow+Semi+Condensed:wght@500;600;700&display=swap">
<style>
:root{
  --board-light:#e6e6e6;
  --board-dark:#b9b9b9;
  --frame:#ffffff;
  --teal-dark:#0f465a;
  --teal-mid:#1d6a80;
  --cyan:#1ec8dc;
  --cyan-light:#8ee8f4;
  --sky-top:#4b93d8;
  --orange:#f28a36;
  --orange-deep:#e8702a;
  --orange-light:#f5a25a;
  --red-poster:#b8402e;
  --blue-poster:#4f88a0;
  --yellow:#f3c21a;
  --purple:#7b2c7e;
  --purple-soft:#9a5a9c;
  --hotel-brown:#8a3e2c;
  --panel-grey:#e9e9ea;
  --white:#ffffff;
}
*{margin:0;padding:0;box-sizing:border-box}
html,body{width:1200px;height:1000px;overflow:hidden}
body{
  background:radial-gradient(ellipse at 50% 45%,var(--board-light) 0%,var(--board-dark) 100%);
  font-family:"Barlow",sans-serif;color:var(--white);position:relative;
}
.screen{position:absolute;width:255px;height:453px;border:5px solid var(--frame);overflow:hidden;background:var(--white)}
.screen > *{position:absolute}
.photo{display:block}
.sidebar{left:0;top:0;width:59px;height:100%}
.c{text-align:center;left:0;width:100%}
.num{font-family:"Barlow Semi Condensed",sans-serif;font-weight:700;line-height:1}
.clock{font-family:"Barlow Semi Condensed",sans-serif;font-weight:600;line-height:1}
.small{font-size:5px;letter-spacing:.2px;font-weight:500}
.forecast{left:12px;width:36px}
.forecast .row{display:flex;justify-content:space-between;align-items:center;height:18px;font-size:6px;font-weight:500}
.forecast .tile{width:10px;height:10px;background:var(--cyan);border-radius:1px}
.brand{font-family:"Barlow Semi Condensed",sans-serif;font-weight:700;text-align:center;line-height:1.05}

/* office tower */
.tower .photo{
  left:59px;top:0;width:186px;height:443px;
  background:
    radial-gradient(ellipse 38% 70% at 42% 78%,rgba(225,232,240,.85),rgba(225,232,240,0) 70%),
    radial-gradient(ellipse 30% 55% at 80% 85%,rgba(70,110,150,.7),rgba(70,110,150,0) 70%),
    radial-gradient(ellipse 22% 50% at 15% 80%,rgba(190,205,222,.8),rgba(190,205,222,0) 70%),
    linear-gradient(180deg,#3f8ad4 0%,#5fa0dc 30%,#9fbcd8 55%,#aab8c6 80%,#4f6c88 100%);
}
.tower .sidebar{background:var(--teal-dark)}
.tower .brand{top:50px;left:0;width:59px;color:var(--cyan);font-size:9px}
.tower .brand-mark{top:20px;left:22px;width:15px;height:15px;background:var(--cyan)}
.tower .clock-block{left:59px;width:186px;top:12px;text-align:center}
.tower .time{font-size:36px}
.tower .day{font-size:18px;font-weight:500;line-height:1.05;margin-top:2px}
.directory{left:64px;top:172px;width:177px;height:56px;background:linear-gradient(135deg,rgba(142,232,244,.95),rgba(30,200,220,.9));border:1.5px solid var(--teal-dark);border-top-color:transparent;border-bottom-color:transparent}
.directory .tag{position:absolute;left:58px;top:2px;width:60px;height:12px;background:var(--teal-dark);color:var(--cyan-light);font-family:"Barlow Semi Condensed",sans-serif;font-weight:700;font-size:10px;text-align:center;line-height:12px}
.directory .chev{position:absolute;top:4px}
.directory .cols{position:absolute;top:20px;left:12px;right:8px;display:flex;justify-content:space-between;color:var(--teal-dark);font-family:"Barlow Semi Condensed",sans-serif;font-weight:600;font-size:7.5px;line-height:10px}
.directory .cols div:first-child{text-align:center}
.news{left:64px;top:328px;width:177px;height:110px;background:linear-gradient(135deg,rgba(142,232,244,.95),rgba(30,200,220,.92))}
.news-tag{left:98px;top:319px;width:104px;height:13px;background:var(--teal-dark);color:var(--cyan);font-family:"Barlow Semi Condensed",sans-serif;font-weight:700;font-size:10px;letter-spacing:.6px;text-align:center;line-height:13px}
.news ul{list-style:none;padding:14px 8px 0 10px;color:var(--teal-dark);font-size:7px;font-weight:500;line-height:9.5px}
.news li{margin-bottom:10px}
.news li::before{content:"· "}

/* mall */
.mall .sidebar{background:var(--orange);height:303px}
.mall .brandbar{left:59px;top:0;width:130px;height:55px;background:linear-gradient(180deg,#4d5866 0%,#3a4048 55%,#2a2f36 100%)}
.mall .brandbar .brand{position:absolute;left:0;top:20px;width:100%;font-size:13px;color:var(--orange-light);font-weight:600}
.mall .timebox{left:189px;top:0;width:56px;height:55px;background:var(--orange);text-align:center;padding-top:10px}
.mall .timebox .time{font-size:15px}
.mall .timebox .day{font-size:8px;font-weight:500;line-height:9px;font-family:"Barlow Semi Condensed",sans-serif}
.mall .ad{left:59px;top:56px;width:186px;height:247px;
  background:
    radial-gradient(ellipse 30% 12% at 50% 55%,rgba(255,255,255,.75),rgba(255,255,255,0) 80%),
    radial-gradient(ellipse 10% 28% at 38% 35%,rgba(200,40,40,.6),rgba(200,40,40,0) 80%),
    radial-gradient(circle at 50% 45%,var(--orange-light),var(--orange-deep))}
.mall .video{left:0;top:304px;width:245px;height:139px;
  background:
    linear-gradient(180deg,rgba(0,0,0,0) 70%,#b23a2a 70%,#b23a2a 76%,#f1f1f1 76%,#f1f1f1 84%,#1c1c1c 84%),
    radial-gradient(ellipse 22% 50% at 50% 60%,#3a2a24,rgba(58,42,36,0) 80%),
    linear-gradient(90deg,#2f4a2c 0%,#55705a 40%,#c9ccd0 70%,#6d7a70 100%)}
.forecast.light .tile{background:var(--orange-light);border:1px solid #fcd8b0}
.mall2 .posters-a{left:0;top:0;width:122px;height:165px;background:radial-gradient(ellipse 40% 25% at 55% 65%,#25323a,rgba(37,50,58,0) 80%),var(--blue-poster)}
.mall2 .posters-b{left:123px;top:0;width:122px;height:165px;background:radial-gradient(ellipse 45% 15% at 50% 70%,#5a1e16,rgba(90,30,22,0) 80%),var(--red-poster)}
.mall2 .levelbox{left:0;top:167px;width:61px;height:92px;background:var(--orange)}
.mall2 .infobox{left:62px;top:167px;width:183px;height:92px;background:var(--orange)}
.mall2 .ad{left:0;top:260px;width:245px;height:183px;
  background:
    radial-gradient(ellipse 22% 16% at 55% 42%,#f7e04a,rgba(247,224,74,0) 90%),
    radial-gradient(ellipse 14% 14% at 42% 44%,#8a9a6a,rgba(138,154,106,0) 90%),
    radial-gradient(ellipse at 50% 40%,#f8d54a,var(--yellow) 60%,#e7a912)}
.mall2 .corner{width:8px;height:8px;border-color:var(--orange-deep);border-style:solid}

/* hotel */
.hotel .photo{left:0;top:0;width:245px;height:443px}
.hotel .logo-panel{left:0;top:0;width:59px;height:105px;background:rgba(233,233,234,.95)}
.hotel .brand{color:var(--hotel-brown);font-size:11px;font-weight:600}
.hotel .levelbox{left:0;top:105px;width:59px;height:60px;background:var(--purple)}
.hotel .ticker{left:0;top:432px;width:245px;height:11px;background:var(--purple);font-size:5.5px;font-weight:600;line-height:11px;white-space:nowrap;letter-spacing:.3px}
.hotel2 .header{left:0;top:0;width:245px;height:45px;background:var(--panel-grey);border-bottom:2px solid var(--purple)}
.hotel2 .header .brand{position:absolute;top:12px;left:0;width:100%;font-size:10px;color:var(--hotel-brown);font-weight:600}
.hotel2 .weatherbox{left:0;top:145px;width:59px;height:106px;background:rgba(241,238,242,.95);color:var(--purple)}
.hotel2 .promo{top:297px;width:115px;height:135px;background:linear-gradient(160deg,#8a8a8a,#2b2b2b)}
.hotel2 .promo-label{top:432px;width:120px;height:11px;background:var(--purple);font-family:"Barlow Semi Condensed",sans-serif;font-weight:600;font-size:8px;text-align:center;line-height:11px}
.promo p{position:absolute;left:4px;top:28px;width:60px;font-size:7px;font-weight:600;line-height:7.5px;color:var(--white)}
</style>
</head>
<body>

<!-- Office tower · lobby B1 -->
<section class="screen tower" style="left:336px;top:32px">
  <div class="photo" role="img" aria-label="Photo of glass skyscrapers against a blue sky"></div>
  <aside class="sidebar">
    <div class="brand-mark" style="position:absolute"></div>
    <div class="brand" style="position:absolute">Northgate<br>Properties</div>
    <svg style="position:absolute;left:8px;top:92px" width="43" height="34" viewBox="0 0 43 34"><polygon points="21.5,0 43,34 21.5,26 0,34" fill="var(--teal-mid)"/></svg>
    <div class="num c" style="position:absolute;top:152px;font-size:44px">B1</div>
    <svg style="position:absolute;left:8px;top:215px" width="43" height="34" viewBox="0 0 43 34"><polygon points="0,0 21.5,8 43,0 21.5,34" fill="var(--white)"/></svg>
    <svg style="position:absolute;left:16px;top:280px" width="28" height="22" viewBox="0 0 28 22"><g fill="none" stroke="#fff" stroke-width="1.6"><circle cx="17" cy="9" r="4.5"/><path d="M17 1v2M24 9h2M22.5 3.5l1.4-1.4M22.5 14.5l1.4 1.4"/><path d="M5 20h15a4 4 0 0 0 0-8 6 6 0 0 0-11-1 4.5 4.5 0 0 0-4 9z" fill="var(--teal-dark)"/></g></svg>
    <div class="small c" style="position:absolute;top:305px">PARTLY COLD</div>
    <div class="num c" style="position:absolute;top:315px;font-size:27px">26°</div>
    <div class="small c" style="position:absolute;top:344px">H 31 ° L 25 °</div>
    <div class="forecast" style="position:absolute;top:361px">
      <div class="row"><span>TUE</span><span class="tile"></span></div>
      <div class="row"><span>WED</span><span class="tile"></span></div>
      <div class="row"><span>THU</span><span class="tile"></span></div>
    </div>
  </aside>
  <div class="clock-block">
    <div class="clock time">12:59</div>
    <div class="day">MONDAY<br>22 APRIL</div>
  </div>
</section>

<!-- Office tower · level 2 -->
<section class="screen tower" style="left:610px;top:32px">
  <div class="photo" role="img" aria-label="Photo of glass skyscrapers against a blue sky"></div>
  <aside class="sidebar">
    <div class="brand-mark" style="position:absolute"></div>
    <div class="brand" style="position:absolute">Northgate<br>Properties</div>
    <svg style="position:absolute;left:8px;top:92px" width="43" height="34" viewBox="0 0 43 34"><polygon points="21.5,0 43,34 21.5,26 0,34" fill="var(--white)"/></svg>
    <div class="num c" style="position:absolute;top:152px;font-size:44px">2</div>
    <svg style="position:absolute;left:8px;top:215px" width="43" height="34" viewBox="0 0 43 34"><polygon points="0,0 21.5,8 43,0 21.5,34" fill="var(--teal-mid)"/></svg>
    <svg style="position:absolute;left:16px;top:280px" width="28" height="22" viewBox="0 0 28 22"><g fill="none" stroke="#fff" stroke-width="1.6"><circle cx="17" cy="9" r="4.5"/><path d="M17 1v2M24 9h2M22.5 3.5l1.4-1.4M22.5 14.5l1.4 1.4"/><path d="M5 20h15a4 4 0 0 0 0-8 6 6 0 0 0-11-1 4.5 4.5 0 0 0-4 9z" fill="var(--teal-dark)"/></g></svg>
    <div class="small c" style="position:absolute;top:305px">PARTLY COLD</div>
    <div class="num c" style="position:absolute;top:315px;font-size:27px">26°</div>
    <div class="small c" style="position:absolute;top:344px">H 31 ° L 25 °</div>
    <div class="forecast" style="position:absolute;top:361px">
      <div class="row"><span>TUE</span><span class="tile"></span></div>
      <div class="row"><span>WED</span><span class="tile"></span></div>
      <div class="row"><span>THU</span><span class="tile"></span></div>
    </div>
  </aside>
  <div class="clock-block">
    <div class="clock time">12:59</div>
    <div class="day">MONDAY<br>22 APRIL</div>
  </div>
  <div class="directory">
    <svg class="chev" style="left:44px" width="11" height="8" viewBox="0 0 11 8"><path d="M5 0.5L1.5 4L5 7.5M10 0.5L6.5 4L10 7.5" fill="none" stroke="var(--teal-dark)" stroke-width="1.6"/></svg>
    <div class="tag">LEVEL 2</div>
    <svg class="chev" style="left:122px" width="11" height="8" viewBox="0 0 11 8"><path d="M1 0.5L4.5 4L1 7.5M6 0.5L9.5 4L6 7.5" fill="none" stroke="var(--teal-dark)" stroke-width="1.6"/></svg>
    <div class="cols">
      <div>ARDEN GLOBAL<br>BOLT LEASING<br>AGELINE INS.</div>
      <div>FASTLANE CORP<br>KESTREL CABLES<br>BRIGHTWORKS IND</div>
    </div>
  </div>
  <div class="news">
    <ul>
      <li>Soaring prices dampens consumer moods ahead of festive season</li>
      <li>Nearly 200 perish in Nepal floods, rescue efforts underway</li>
      <li>Analyst cuts corporate earnings estimates on growth concerns</li>
    </ul>
  </div>
  <div class="news-tag">BREAKING NEWS</div>
</section>

<!-- Shopping mall · level 19 -->
<section class="screen mall" style="left:54px;top:516px">
  <aside class="sidebar">
    <svg style="position:absolute;left:8px;top:11px" width="43" height="35" viewBox="0 0 43 35"><polygon points="21.5,0 43,35 21.5,27 0,35" fill="var(--white)"/></svg>
    <div class="num c" style="position:absolute;top:57px;font-size:40px">19</div>
    <svg style="position:absolute;left:8px;top:106px" width="43" height="31" viewBox="0 0 43 31"><polygon points="0,0 21.5,8 43,0 21.5,31" fill="var(--orange-light)"/></svg>
    <svg style="position:absolute;left:16px;top:158px" width="28" height="22" viewBox="0 0 28 22"><g fill="none" stroke="#fff" stroke-width="1.6"><circle cx="17" cy="9" r="4.5"/><path d="M17 1v2M24 9h2M22.5 3.5l1.4-1.4M22.5 14.5l1.4 1.4"/><path d="M5 20h15a4 4 0 0 0 0-8 6 6 0 0 0-11-1 4.5 4.5 0 0 0-4 9z" fill="var(--orange)"/></g></svg>
    <div class="small c" style="position:absolute;top:183px">PARTLY COLD</div>
    <div class="num c" style="position:absolute;top:193px;font-size:27px">26°</div>
    <div class="small c" style="position:absolute;top:222px">H 31 ° L 25 °</div>
    <div class="forecast light" style="position:absolute;top:237px">
      <div class="row"><span>TUE</span><span class="tile"></span></div>
      <div class="row"><span>WED</span><span class="tile"></span></div>
      <div class="row"><span>THU</span><span class="tile"></span></div>
    </div>
  </aside>
  <div class="brandbar" role="img" aria-label="Dusk city skyline behind the tenant name"><div class="brand">Swiftline</div></div>
  <div class="timebox">
    <div class="clock time">12:59</div>
    <div class="day">MONDAY<br>22 APRIL</div>
  </div>
  <div class="ad" role="img" aria-label="Orange advertisement with skis in a heap of snow and a winter clothing slogan"></div>
  <div class="video" role="img" aria-label="Live television news broadcast with lower-third headline banner"></div>
</section>

<!-- Shopping mall · level 12 -->
<section class="screen mall2" style="left:328px;top:516px">
  <div class="posters-a" role="img" aria-label="Blue poster with tangled cassette tape and a song lyric"></div>
  <div class="posters-b" role="img" aria-label="Red poster with a vinyl record trailing tape and a song lyric"></div>
  <div class="levelbox">
    <svg style="position:absolute;left:6px;top:12px" width="48" height="17" viewBox="0 0 48 17"><polygon points="12,0 24,17 12,12 0,17" fill="var(--white)"/><polygon points="24,0 36,5 48,0 36,17" fill="var(--orange-light)"/></svg>
    <div class="num c" style="position:absolute;top:38px;font-size:46px">12</div>
  </div>
  <div class="infobox">
    <div class="clock" style="position:absolute;left:28px;top:16px;width:70px;text-align:center;font-size:19px">12:59</div>
    <div style="position:absolute;left:28px;top:37px;width:70px;text-align:center;font-family:'Barlow Semi Condensed',sans-serif;font-weight:500;font-size:10px;line-height:10.5px">MONDAY<br>22 APRIL</div>
    <div style="position:absolute;left:36px;top:61px;width:56px;display:flex;justify-content:space-between;font-size:5px">
      <span style="text-align:center">TUE<br><span style="display:inline-block;width:9px;height:9px;background:var(--orange-light);border:1px solid #fcd8b0;margin-top:2px"></span></span>
      <span style="text-align:center">WED<br><span style="display:inline-block;width:9px;height:9px;background:var(--orange-light);border:1px solid #fcd8b0;margin-top:2px"></span></span>
      <span style="text-align:center">THU<br><span style="display:inline-block;width:9px;height:9px;background:var(--orange-light);border:1px solid #fcd8b0;margin-top:2px"></span></span>
    </div>
    <svg style="position:absolute;left:137px;top:10px" width="30" height="22" viewBox="0 0 28 22"><g fill="none" stroke="#fff" stroke-width="1.6"><circle cx="17" cy="9" r="4.5"/><path d="M17 1v2M24 9h2M22.5 3.5l1.4-1.4M22.5 14.5l1.4 1.4"/><path d="M5 20h15a4 4 0 0 0 0-8 6 6 0 0 0-11-1 4.5 4.5 0 0 0-4 9z" fill="var(--orange)"/></g></svg>
    <div class="small" style="position:absolute;left:128px;top:36px;width:50px;text-align:center">PARTLY COLD</div>
    <div class="num" style="position:absolute;left:128px;top:46px;width:54px;text-align:center;font-size:28px">26°</div>
    <div class="small" style="position:absolute;left:128px;top:77px;width:54px;text-align:center">H 31 ° L 25 °</div>
  </div>
  <div class="ad" role="img" aria-label="Yellow appliance advertisement with a half-mouldy lemon and a freshness slogan"></div>
  <div class="corner" style="left:2px;top:262px;border-width:2px 0 0 2px"></div>
  <div class="corner" style="right:2px;top:262px;border-width:2px 2px 0 0"></div>
  <div class="corner" style="left:2px;bottom:2px;border-width:0 0 2px 2px"></div>
  <div class="corner" style="right:2px;bottom:2px;border-width:0 2px 2px 0"></div>
</section>

<!-- Hotel · lobby B1 -->
<section class="screen hotel" style="left:618px;top:516px">
  <div class="photo" role="img" aria-label="Photo of an ornate hotel lobby with armchairs, carved archway and a flower arrangement" style="background:
    radial-gradient(ellipse 30% 18% at 40% 62%,rgba(235,215,160,.8),rgba(235,215,160,0) 80%),
    radial-gradient(ellipse 40% 22% at 75% 85%,rgba(230,130,80,.85),rgba(230,130,80,0) 80%),
    radial-gradient(ellipse 35% 20% at 55% 42%,rgba(120,80,55,.9),rgba(120,80,55,0) 80%),
    linear-gradient(180deg,#7a5a3c 0%,#a8865e 10%,#5e3e28 22%,#7a5034 45%,#9a6440 65%,#c98654 85%,#d99a66 100%)"></div>
  <div class="logo-panel">
    <div class="brand" style="position:absolute;left:0;top:62px;width:59px">Lorraine<br>Hotels</div>
  </div>
  <div class="levelbox">
    <svg style="position:absolute;left:16px;top:6px" width="28" height="11" viewBox="0 0 28 11"><polygon points="7,0 14,11 7,8 0,11" fill="var(--purple-soft)"/><polygon points="14,0 21,3 28,0 21,11" fill="var(--white)"/></svg>
    <div class="num c" style="position:absolute;top:20px;font-size:34px">B1</div>
  </div>
  <div class="ticker">WELCOME TO LORRAINE HOTELS &nbsp;•&nbsp; WELCOME TO LORRAINE HOTELS &nbsp;•&nbsp; WELCOME TO LORRAINE HOTELS &nbsp;•&nbsp; WELCOME TO LORRAINE HOTELS</div>
</section>

<!-- Hotel · level 4 -->
<section class="screen hotel hotel2" style="left:892px;top:516px">
  <div class="photo" role="img" aria-label="Photo of a warmly lit hotel bar with golden shelving" style="top:45px;height:248px;background:
    radial-gradient(ellipse 30% 25% at 65% 40%,rgba(255,200,90,.85),rgba(255,200,90,0) 80%),
    radial-gradient(ellipse 45% 20% at 55% 80%,rgba(220,150,60,.8),rgba(220,150,60,0) 80%),
    linear-gradient(160deg,#2e1c0c 0%,#6a4418 30%,#b07a30 55%,#4a2e12 80%,#1e1208 100%)"></div>
  <div class="header"><div class="brand">Lorraine<br>Hotels</div></div>
  <div class="levelbox" style="top:87px;height:58px">
    <svg style="position:absolute;left:16px;top:6px" width="28" height="11" viewBox="0 0 28 11"><polygon points="7,0 14,11 7,8 0,11" fill="var(--purple-soft)"/><polygon points="14,0 21,3 28,0 21,11" fill="var(--white)"/></svg>
    <div class="num c" style="position:absolute;top:20px;font-size:34px">4</div>
  </div>
  <div class="weatherbox">
    <svg style="position:absolute;left:16px;top:10px" width="28" height="22" viewBox="0 0 28 22"><g fill="none" stroke="var(--purple)" stroke-width="1.6"><circle cx="17" cy="9" r="4.5"/><path d="M17 1v2M24 9h2M22.5 3.5l1.4-1.4M22.5 14.5l1.4 1.4"/><path d="M5 20h15a4 4 0 0 0 0-8 6 6 0 0 0-11-1 4.5 4.5 0 0 0-4 9z" fill="#f1eef2"/></g></svg>
    <div class="small c" style="position:absolute;top:35px">PARTLY COLD</div>
    <div class="num c" style="position:absolute;top:45px;font-size:27px">26°</div>
    <div class="small c" style="position:absolute;top:74px">H 31 ° L 25 °</div>
  </div>
  <div class="promo" style="left:3px;background:radial-gradient(ellipse 35% 45% at 70% 40%,#9a9a9a,rgba(154,154,154,0) 80%),linear-gradient(160deg,#5a5a5a,#1e1e1e)" role="img" aria-label="Black and white photo of a diner savouring fine food"><p>Indulge your love of fine food</p></div>
  <div class="promo" style="left:127px;background:radial-gradient(ellipse 35% 45% at 70% 45%,#b5b5b5,rgba(181,181,181,0) 80%),linear-gradient(160deg,#4a4a4a,#1a1a1a)" role="img" aria-label="Black and white photo of a blindfolded chef tasting a dish"><p style="top:14px;width:58px;font-size:6px;line-height:6.5px">The ultimate sensory adventure, taste the unseen</p></div>
  <div class="promo-label" style="left:0">TEXT ADS 1 HERE</div>
  <div class="promo-label" style="left:124px;width:121px">TEXT ADS 2 HERE</div>
</section>

</body>
</html>
```